Fenmarrow brand new master design

Company Background:
The company Fenmarrow was founded in March 2019 and deals with the IT of the smallest companies. Unlike the PC specialist, no server is needed. Our motto is "just work". This motto aims to make it easy for the user to work without having to deal with the problems of PCs or a main computer.

This project:
We would like to create a Powerpoint Master wich makes us able to create future presentations. We'll need a design to ge it done. We are looking for a design aligned with our website and logo.

Target Market(s)

In a more complicated IT infrastructure it is even harder for small companies to maintain it. Even plumbers, electricians should be able to get a secure and reliable IT infrastructure. We are targeting companies between 1 and 15 IT users. Our customers do not have any ERP software that's just so simple. There is no need to have things like a server onsite anymore. We are providing the service from a safe and secure location within Germany.

Industry/Entity Type

It Company

Other font styles liked:
• Raleway

Requirements
Must have
• What we need to be in the master:
- Title Page (first slide)
- Table of content page
- Subtopic title page (Title with underline)
- Content-PAge with bullet points
- Content split bullet-points and image

We are using Raleway Google font.
Logos attached. Our website: www.fenmarrow.de
Must be aligned to our website and logo.
Nice to have
• selected Stock image gallery

```html
<!DOCTYPE html>
<html lang="de">
<head>
<meta charset="utf-8">
<title>Fenmarrow – Präsentationsmaster</title>
<link href="https://fonts.googleapis.com/css2?family=Raleway:wght@400;500;600;700;800&display=swap" rel="stylesheet">
<style>
:root{
  --ink:#231f20;
  --blue:#0a6fc2;
  --paper:#ffffff;
  --mist:#eef0f6;
  --text:#2b2b2b;
  --frame:#c9c9cc;
}
*{margin:0;padding:0;box-sizing:border-box}
html,body{width:1200px;height:1080px;overflow:hidden;background:#fff}
body{position:relative;font-family:'Raleway',sans-serif;color:var(--text)}
.slide{position:absolute;width:364px;height:274px;overflow:hidden;background:var(--paper);border:1px solid var(--frame)}
.abs{position:absolute}
.brand{position:absolute;font-family:'Raleway',sans-serif;font-weight:700;letter-spacing:1.5px;color:var(--blue);display:flex;align-items:center;gap:5px;white-space:nowrap}
.brand .dot{width:7px;height:7px;background:var(--blue);display:inline-block}
.brand.light{color:#fff}
.brand.light .dot{background:#fff}
.photo{position:absolute}
.mon{width:11px;height:10px;flex:none}
.h-title{font-weight:800;color:var(--ink);line-height:1.1;letter-spacing:.2px}
.accent{position:absolute;width:4px;background:var(--blue)}
.copy{font-size:5.6px;line-height:1.45;color:#333}
.blob{position:absolute;background:var(--mist);border-radius:48% 52% 40% 60%/55% 45% 55% 45%}

/* title slide */
.s-title{left:43px;top:113px;background:var(--ink)}
.s-title .photo{left:0;top:22px;width:346px;height:234px;background:radial-gradient(ellipse at 55% 40%,#4a4f5a 0%,#30343c 55%,#24272d 100%);border:1px solid var(--blue)}

/* toc */
.s-toc{left:417px;top:113px}
.s-toc .side{left:0;top:0;width:27px;height:100%;background:var(--ink)}
.toc-list{position:absolute;left:45px;top:76px;list-style:none}
.toc-list li{display:flex;align-items:center;gap:7px;height:16.7px;font-size:10px;font-weight:500;color:var(--ink)}

/* intro split */
.s-intro{left:793px;top:113px}
.s-intro .side{left:0;top:0;width:81px;height:100%;background:var(--ink)}
.s-intro .photo{left:15px;top:110px;width:125px;height:108px;background:linear-gradient(135deg,#e9e6e2,#c9bfb3 55%,#b4573a);box-shadow:2px 2px 0 var(--blue)}
.s-intro .copy p{margin-bottom:6px;text-align:justify}

/* it slide */
.s-it{left:43px;top:404px}
.s-it .side{left:221px;top:0;width:143px;height:100%;background:var(--ink)}
.it-copy{position:absolute;left:18px;width:180px;text-align:center}
.btn{position:absolute;left:205px;width:137px;height:37px;background:var(--blue);color:#fff;display:flex;align-items:center;gap:9px;padding-left:13px;font-size:11px;font-weight:600}
.btn svg{width:18px;height:18px}

/* bullets */
.s-bullets{left:417px;top:404px}
.s-bullets .dark{left:0;top:0;width:100%;height:237px;background:var(--ink)}
.bl-title{position:absolute;left:28px;top:12px;font-size:15.5px;font-weight:800;color:#fff;white-space:nowrap}
.bl-rule{position:absolute;left:28px;top:34px;width:307px;height:1.5px;background:var(--blue)}
.bl-item{position:absolute;left:28px;width:312px;display:flex;gap:11px;font-size:6.4px;line-height:1.3;color:#f2f2f2}
.bl-item .mon{margin-top:0}

/* benefits */
.s-benefit{left:793px;top:404px}
.s-benefit .head{left:0;top:0;width:100%;height:38px;background:var(--ink)}
.tile{position:absolute;width:84px;text-align:center}
.tile .ico{width:33px;height:33px;margin:0 auto;background:var(--blue);display:flex;align-items:center;justify-content:center}
.tile .ico svg{width:18px;height:18px}
.tile h4{font-size:6.6px;font-weight:700;color:var(--ink);margin-top:5px}
.tile p{font-size:4.7px;line-height:1.3;color:#444;margin-top:2px;padding:0 4px}

/* founder */
.s-founder{left:43px;top:693px}
.fd-item{position:absolute;left:18px;width:250px;display:flex;gap:7px;font-size:6.6px;line-height:1.25;color:var(--ink)}
.s-founder .photo{left:274px;top:39px;width:90px;height:196px;background:linear-gradient(180deg,#f1f1f1 0%,#e3e3e5 45%,#2a2f3d 70%,#1f2330 100%)}
.quote-band{position:absolute;left:0;top:180px;width:274px;height:7px;background:var(--blue)}
.quote{position:absolute;left:0;top:187px;width:274px;height:48px;background:var(--ink);color:#fff;font-size:10.2px;font-weight:700;line-height:1.75;text-align:center;padding-top:5px}

/* thanks */
.s-thanks{left:417px;top:693px;background:var(--ink);border-color:var(--ink)}
.thanks{position:absolute;left:0;top:28px;width:100%;text-align:center;font-size:31px;font-weight:800;color:#fff;letter-spacing:.5px}
.s-thanks .photo{left:37px;top:109px;width:140px;height:77px;background:linear-gradient(90deg,#3c4552 0%,#8d96a3 45%,#eef0f2 75%,#ffffff)}
.vline{position:absolute;left:200px;top:96px;width:2px;height:108px;background:var(--blue)}
.contact{position:absolute;left:218px;display:flex;align-items:center;gap:9px;font-size:8px;color:#fff}
.contact .ci{width:13px;height:13px;border-radius:50%;background:var(--blue);display:flex;align-items:center;justify-content:center}
.contact .ci svg{width:8px;height:8px}
</style>
</head>
<body>
<svg width="0" height="0" style="position:absolute">
  <defs>
    <symbol id="mon" viewBox="0 0 22 20"><path d="M2 2h18v12H4v4m-2-16v12" fill="none" stroke="#0a6fc2" stroke-width="2.4" stroke-linecap="round" stroke-linejoin="round"/><path d="M7 18h9" stroke="#0a6fc2" stroke-width="2.4" stroke-linecap="round"/></symbol>
  </defs>
</svg>

<!-- Title -->
<section class="slide s-title">
  <div class="photo" role="img" aria-label="Dunkles Foto: Hand berührt ein leuchtendes Sicherheitsschild mit Schloss"></div>
  <div class="brand light" style="left:70px;top:122px;font-size:24px"><span class="dot"></span>FENMARROW</div>
</section>

<!-- Table of content -->
<section class="slide s-toc">
  <div class="blob" style="left:210px;top:-30px;width:190px;height:230px"></div>
  <div class="abs side"></div>
  <div class="abs h-title" style="left:45px;top:34px;font-size:16.5px">TABLE OF CONTENT</div>
  <ul class="toc-list">
    <li><svg class="mon"><use href="#mon"/></svg>HOME</li>
    <li><svg class="mon"><use href="#mon"/></svg>ABOUT US</li>
    <li><svg class="mon"><use href="#mon"/></svg>MESSAGE FROM FOUNDER</li>
    <li><svg class="mon"><use href="#mon"/></svg>OUR SERVICES</li>
    <li><svg class="mon"><use href="#mon"/></svg>SOLUTIONS</li>
    <li><svg class="mon"><use href="#mon"/></svg>OUR PARTNERS</li>
    <li><svg class="mon"><use href="#mon"/></svg>TESTIMONIALS</li>
    <li><svg class="mon"><use href="#mon"/></svg>CONTACT US</li>
  </ul>
  <div class="brand" style="left:210px;top:242px;font-size:15px"><span class="dot"></span>FENMARROW</div>
</section>

<!-- Intro split -->
<section class="slide s-intro">
  <div class="blob" style="left:250px;top:20px;width:130px;height:170px"></div>
  <div class="abs side"></div>
  <div class="brand" style="left:18px;top:70px;font-size:13px"><span class="dot"></span>FENMARROW</div>
  <div class="photo" role="img" aria-label="Foto: zwei Kolleginnen besprechen sich an einem Tisch im hellen Büro"></div>
  <div class="abs h-title" style="left:158px;top:42px;font-size:15.5px">EINFACH, ZUVERLÄSSIG<br>UND GÜNSTIG</div>
  <div class="abs copy" style="left:161px;top:101px;width:184px">
    <p>Große Unternehmen arbeiten schon seit Jahren so und konnten damit ihre Kosten senken und die Stabilität erhöhen. Jetzt bietet Fenmarrow die Lösung auch für kleinste Unternehmen an. Wir speichern Ihre Daten dauerhaft an einem sicheren Ort. Notwendige Sicherheitsvorkehrungen werden getroffen und Sie konzentrieren sich auf Ihr tägliches Geschäft.</p>
    <p>Große Unternehmen arbeiten schon seit Jahren so und konnten damit ihre Kosten senken und die Stabilität erhöhen. Jetzt bietet Fenmarrow die Lösung auch für kleinste Unternehmen an. Wir speichern Ihre Daten dauerhaft an einem sicheren Ort. Notwendige Sicherheitsvorkehrungen werden getroffen und Sie konzentrieren sich auf Ihr tägliches Geschäft.</p>
    <p>Große Unternehmen arbeiten schon seit Jahren so und konnten damit ihre Kosten senken und die Stabilität erhöhen.</p>
  </div>
</section>

<!-- IT, die einfach funktioniert -->
<section class="slide s-it">
  <div class="abs side"></div>
  <div class="accent" style="left:19px;top:22px;height:34px"></div>
  <div class="abs h-title" style="left:36px;top:21px;font-size:16px">IT, DIE EINFACH<br>FUNKTIONIERT</div>
  <p class="copy it-copy" style="top:81px">Die Basis der IT-Probleme, die Ihren Geschäftsalltag unnötig erschweren, ist – neben dem menschlichen Faktor – der Rechner selbst, denn dort landen Viren, werden Programme lahm und gehen Daten verloren.</p>
  <p class="copy it-copy" style="top:134px">Die Basis der IT-Probleme, die Ihren Geschäftsalltag unnötig erschweren, ist – neben dem menschlichen Faktor – der Rechner selbst, denn dort landen Viren, werden Programme lahm und gehen Daten verloren.</p>
  <p class="copy it-copy" style="top:186px">Die Basis der IT-Probleme, die Ihren Geschäftsalltag unnötig erschweren, ist – neben dem menschlichen Faktor – der Rechner selbst, denn dort landen Viren, werden Programme lahm und gehen Daten verloren.</p>
  <div class="btn" style="top:80px"><svg viewBox="0 0 24 24"><path d="M12 3 3 20h18L12 3Zm0 5v13" fill="none" stroke="#fff" stroke-width="2" stroke-linejoin="round"/></svg>Das Problem</div>
  <div class="btn" style="top:133px"><svg viewBox="0 0 24 24"><path d="M12 2a7 7 0 0 0-4 12.7V18h8v-3.3A7 7 0 0 0 12 2Zm-3 18h6v2H9z" fill="#fff"/></svg>Unsere Lösung</div>
  <div class="btn" style="top:185px"><svg viewBox="0 0 24 24"><path d="M12 2 4 5v6c0 5 3.4 9.4 8 11 4.6-1.6 8-6 8-11V5l-8-3Z" fill="#fff"/><path d="M12 5v14" stroke="#0a6fc2" stroke-width="2"/></svg>Ihre Sicherheit</div>
  <div class="brand" style="left:12px;top:243px;font-size:15px"><span class="dot"></span>FENMARROW</div>
</section>

<!-- Bullet content -->
<section class="slide s-bullets">
  <div class="abs dark"></div>
  <div class="bl-title">EINFACH, ZUVERLÄSSIG UND GÜNSTIG</div>
  <div class="bl-rule"></div>
  <div class="bl-item" style="top:54px"><svg class="mon"><use href="#mon"/></svg><span>Große Unternehmen arbeiten schon seit Jahren so und konnten damit ihre Kosten senken und die Stabilität erhöhen.</span></div>
  <div class="bl-item" style="top:78px"><svg class="mon"><use href="#mon"/></svg><span>Jetzt bietet Fenmarrow die Lösung auch für kleinste Unternehmen an. Wir speichern Ihre Daten dauerhaft an einem sicheren Ort. Notwendige Sicherheitsvorkehrungen werden getroffen und Sie konzentrieren sich auf Ihr tägliches Geschäft.</span></div>
  <div class="bl-item" style="top:111px"><svg class="mon"><use href="#mon"/></svg><span>Große Unternehmen arbeiten schon seit Jahren so und konnten damit ihre Kosten senken und die Stabilität erhöhen. Jetzt bietet Fenmarrow die Lösung auch für kleinste Unternehmen an. Wir speichern Ihre Daten dauerhaft an einem sicheren Ort. Notwendige Sicherheitsvorkehrungen werden getroffen und Sie konzentrieren sich auf Ihr tägliches Geschäft.</span></div>
  <div class="bl-item" style="top:151px"><svg class="mon"><use href="#mon"/></svg><span>Große Unternehmen arbeiten schon seit Jahren so und konnten damit ihre Kosten senken und die Stabilität erhöhen. Jetzt bietet Fenmarrow die Lösung auch für kleinste Unternehmen an. Wir speichern Ihre Daten dauerhaft an einem sicheren Ort. Notwendige Sicherheitsvorkehrungen werden getroffen und Sie konzentrieren sich auf Ihr tägliches Geschäft.</span></div>
  <div class="bl-item" style="top:191px"><svg class="mon"><use href="#mon"/></svg><span>Große Unternehmen arbeiten schon seit Jahren so und konnten damit ihre Kosten senken und die Stabilität erhöhen. Jetzt bietet Fenmarrow die Lösung auch für kleinste Unternehmen an.</span></div>
  <div class="brand" style="left:108px;top:243px;font-size:15px"><span class="dot"></span>FENMARROW</div>
</section>

<!-- Benefits grid -->
<section class="slide s-benefit">
  <div class="blob" style="left:-10px;top:95px;width:380px;height:170px;border-radius:40%"></div>
  <div class="abs head"></div>
  <div class="brand light" style="left:17px;top:12px;font-size:14px"><span class="dot"></span>FENMARROW</div>
  <div class="accent" style="left:19px;top:51px;height:19px"></div>
  <div class="abs h-title" style="left:33px;top:51px;font-size:15.5px">IHR NUTZEN IM ÜBERBLICK</div>

  <div class="tile" style="left:16px;top:87px"><div class="ico"><svg viewBox="0 0 24 24"><circle cx="12" cy="14" r="7" fill="none" stroke="#fff" stroke-width="2"/><path d="M12 14V10M10 3h4" stroke="#fff" stroke-width="2"/></svg></div><h4>Expressentstörung</h4><p>Montags bis Freitags erfolgt die Störungsbehebung in maximal 8 Stunden durch den Fenmarrow Support</p></div>
  <div class="tile" style="left:100px;top:87px"><div class="ico"><svg viewBox="0 0 24 24"><path d="M12 2c3 3 4 7 3 12H9C8 9 9 5 12 2Zm-3 12-3 4h3m6-4 3 4h-3m-5 2h4v2h-4z" fill="#fff"/></svg></div><h4>Expressentstörung</h4><p>Montags bis Freitags erfolgt die Störungsbehebung in maximal 8 Stunden durch den Fenmarrow Support</p></div>
  <div class="tile" style="left:184px;top:87px"><div class="ico"><svg viewBox="0 0 24 24"><path d="M12 2 4 5v6c0 5 3.4 9.4 8 11 4.6-1.6 8-6 8-11V5l-8-3Z" fill="none" stroke="#fff" stroke-width="2"/><path d="m8.5 12 2.5 2.5 4.5-5" fill="none" stroke="#fff" stroke-width="2"/></svg></div><h4>Expressentstörung</h4><p>Montags bis Freitags erfolgt die Störungsbehebung in maximal 8 Stunden durch den Fenmarrow Support</p></div>
  <div class="tile" style="left:268px;top:87px"><div class="ico"><svg viewBox="0 0 24 24"><path d="M4 3h16v5H4zm0 6.5h16v5H4zM4 16h16v5H4z" fill="none" stroke="#fff" stroke-width="1.6"/><path d="M7 5.5h6M7 12h6M7 18.5h6" stroke="#fff" stroke-width="1.6"/></svg></div><h4>Expressentstörung</h4><p>Montags bis Freitags erfolgt die Störungsbehebung in maximal 8 Stunden durch den Fenmarrow Support</p></div>

  <div class="tile" style="left:16px;top:173px"><div class="ico"><svg viewBox="0 0 24 24"><path d="M12 3v12M7 8h10M4 13c2 3 5 4 8 4s6-1 8-4M3 20c2 1 3 1 4.5 0s3-1 4.5 0 3 1 4.5 0 3-1 4.5 0" fill="none" stroke="#fff" stroke-width="1.8"/></svg></div><h4>Expressentstörung</h4><p>Montags bis Freitags erfolgt die Störungsbehebung in maximal 8 Stunden durch den Fenmarrow Support</p></div>
  <div class="tile" style="left:100px;top:173px"><div class="ico"><svg viewBox="0 0 24 24"><path d="M5 4h14v11H5zM2 18h20v2H2z" fill="none" stroke="#fff" stroke-width="1.8"/><circle cx="12" cy="9.5" r="3" fill="none" stroke="#fff" stroke-width="1.6"/></svg></div><h4>Expressentstörung</h4><p>Montags bis Freitags erfolgt die Störungsbehebung in maximal 8 Stunden durch den Fenmarrow Support</p></div>
  <div class="tile" style="left:184px;top:173px"><div class="ico"><svg viewBox="0 0 24 24"><path d="M19 9a7 7 0 0 0-13-2M5 15a7 7 0 0 0 13 2" fill="none" stroke="#fff" stroke-width="2.2"/><path d="M20 4v5h-5M4 20v-5h5" fill="none" stroke="#fff" stroke-width="2.2"/></svg></div><h4>Expressentstörung</h4><p>Montags bis Freitags erfolgt die Störungsbehebung in maximal 8 Stunden durch den Fenmarrow Support</p></div>
  <div class="tile" style="left:268px;top:173px"><div class="ico"><svg viewBox="0 0 24 24"><rect x="8" y="8" width="8" height="8" fill="none" stroke="#fff" stroke-width="1.8"/><path d="M8 8 4 4M16 8l4-4M8 16l-4 4M16 16l4 4" stroke="#fff" stroke-width="1.6"/><circle cx="4" cy="4" r="1.6" fill="#fff"/><circle cx="20" cy="4" r="1.6" fill="#fff"/><circle cx="4" cy="20" r="1.6" fill="#fff"/><circle cx="20" cy="20" r="1.6" fill="#fff"/></svg></div><h4>Expressentstörung</h4><p>Montags bis Freitags erfolgt die Störungsbehebung in maximal 8 Stunden durch den Fenmarrow Support</p></div>
</section>

<!-- Founder -->
<section class="slide s-founder">
  <div class="accent" style="left:13px;top:22px;height:32px"></div>
  <div class="abs h-title" style="left:29px;top:20px;font-size:16px">Jonas Kellbrand</div>
  <div class="abs" style="left:29px;top:43px;font-size:8px;color:var(--ink)">Gründer und Geschäftsführer</div>
  <div class="fd-item" style="top:76px"><svg class="mon"><use href="#mon"/></svg><span>Jonas ist 34 Jahre alt und ledig.</span></div>
  <div class="fd-item" style="top:92px"><svg class="mon"><use href="#mon"/></svg><span>Seit seiner Ausbildung zum Fachinformatiker und seinem Studium der IT ist er seit über 15 Jahren in der EDV-Branche tätig.</span></div>
  <div class="fd-item" style="top:117px"><svg class="mon"><use href="#mon"/></svg><span>In seiner beruflichen Laufbahn hat er bei namenhaften Firmen wie Norvatek Systems gearbeitet.</span></div>
  <div class="fd-item" style="top:141px"><svg class="mon"><use href="#mon"/></svg><span>Zuletzt hat er erfolgreich Großprojekte im Bereich des IT-Outsourcings mit mehr als 2.000 Arbeitsplätzen geplant und geleitet.</span></div>
  <div class="photo" role="img" aria-label="Porträtfoto des Gründers im dunklen Anzug vor hellem Hintergrund"></div>
  <div class="quote-band"></div>
  <div class="quote">“ Mein Ziel mit Fenmarrow ist es, die IT von<br>kleinsten Unternehmen sicherer zu gestalten. ”</div>
  <div class="brand" style="left:108px;top:245px;font-size:15px"><span class="dot"></span>FENMARROW</div>
</section>

<!-- Thank you -->
<section class="slide s-thanks">
  <div class="thanks">THANK YOU</div>
  <div class="photo" role="img" aria-label="Foto: Techniker mit Laptop im Serverraum"></div>
  <div class="vline"></div>
  <div class="contact" style="top:120px"><span class="ci"><svg viewBox="0 0 24 24"><path d="M6 3h4l2 5-3 2a12 12 0 0 0 5 5l2-3 5 2v4a2 2 0 0 1-2 2A17 17 0 0 1 4 5a2 2 0 0 1 2-2Z" fill="#fff"/></svg></span>+49 2931 508417 0</div>
  <div class="contact" style="top:141px"><span class="ci"><svg viewBox="0 0 24 24"><circle cx="12" cy="12" r="9" fill="none" stroke="#fff" stroke-width="2"/><path d="M3 12h18M12 3c3 3 3 15 0 18M12 3c-3 3-3 15 0 18" fill="none" stroke="#fff" stroke-width="1.6"/></svg></span>www.fenmarrow.de</div>
  <div class="contact" style="top:162px"><span class="ci"><svg viewBox="0 0 24 24"><path d="M3 6h18v12H3z" fill="none" stroke="#fff" stroke-width="2"/><path d="m3 6 9 7 9-7" fill="none" stroke="#fff" stroke-width="2"/></svg></span>kunde@fenmarrow.de</div>
</section>
</body>
</html>
```